Newsletter Ad

I am looking for someone to design an advertisement for a mother's club newsletter. 4" wide X by 5" tall (and 2.5" wide X 5" tall if possible).

I'm a psychotherapist, so want the ad to look professional, but modern. I have a logo with my photo attached that can be incorporated into the design. The colors of my website are turquoise and white. I'd like to keep with that theme...so maybe some turquoise blocking to match the logo font color.

I'm uploading a logo as well as an ad draft with the content I'd like listed in the ad.

```html
<!DOCTYPE html>
<html lang="en">
<head>
<meta charset="utf-8">
<title>Nora Vale, MA, MFT – Newsletter Ad</title>
<link rel="stylesheet" href="https://fonts.googleapis.com/css2?family=Questrial&family=Cinzel:wght@400&family=Comfortaa:wght@400;700&family=Arimo&display=swap">
<style>
  :root {
    --teal-ink: #2a9a9c;
    --teal-panel: #2aabad;
    --white: #ffffff;
    --photo-dark: #1a1511;
    --photo-mid: #8a6a45;
    --photo-light: #c9a77a;
  }
  html, body {
    margin: 0;
    padding: 0;
    overflow: hidden;
    background: var(--white);
  }
  .ad {
    position: relative;
    width: 960px;
    height: 1200px;
    background: var(--white);
    overflow: hidden;
    font-family: "Comfortaa", sans-serif;
    color: var(--teal-ink);
  }
  .ad__title {
    position: absolute;
    left: 0;
    top: 0;
    width: 960px;
    height: 160px;
    margin: 0;
  }
  .ad__title-text {
    font-family: "Questrial", sans-serif;
    font-weight: 400;
    font-size: 104px;
    fill: var(--teal-ink);
  }
  .ad__portrait {
    position: absolute;
    left: 36px;
    top: 193px;
    width: 390px;
    height: 585px;
    background:
      radial-gradient(ellipse 45% 40% at 50% 40%, var(--photo-light) 0%, var(--photo-mid) 55%, transparent 80%),
      linear-gradient(180deg, var(--photo-dark) 0%, #3a2c1e 60%, var(--photo-dark) 100%);
  }
  .contact {
    position: absolute;
    left: 57px;
    top: 834px;
    margin: 0;
    font-style: normal;
  }
  .contact__line {
    display: block;
    font-size: 29px;
    line-height: 43px;
    white-space: nowrap;
  }
  .contact__line--strong {
    font-size: 33px;
    font-weight: 700;
    line-height: 46px;
  }
  .contact__license {
    display: block;
    margin-top: 50px;
    font-family: "Arimo", sans-serif;
    font-size: 29px;
    line-height: 36px;
  }
  .services {
    position: absolute;
    left: 464px;
    top: 193px;
    width: 460px;
    height: 970px;
    background: var(--teal-panel);
    color: var(--white);
    box-sizing: border-box;
    padding: 12px 17px 0 20px;
    text-align: right;
  }
  .services__heading {
    margin: 0;
    font-family: "Cinzel", serif;
    font-weight: 400;
    font-size: 37px;
    line-height: 48.5px;
    letter-spacing: 1px;
    white-space: nowrap;
  }
  .services__rule {
    display: block;
    margin: 6px 0 0 13px;
    width: 406px;
    height: 4px;
  }
  .services__list {
    list-style: none;
    margin: 20px 0 0;
    padding: 0;
    font-size: 33px;
  }
  .services__item {
    line-height: 44px;
    margin-bottom: 43px;
    white-space: nowrap;
  }
</style>
</head>
<body>
<main class="ad">
  <h1 class="ad__title">
    <svg width="960" height="160" viewBox="0 0 960 160" aria-label="Nora Vale, MA, MFT">
      <text class="ad__title-text" x="38" y="130" textLength="880" lengthAdjust="spacingAndGlyphs">NORA VALE,MA, MFT</text>
    </svg>
  </h1>

  <div class="ad__portrait" role="img" aria-label="Portrait photograph of the therapist, smiling, with long light-brown hair against a dark background"></div>

  <address class="contact">
    <span class="contact__line">118 Alder Avenue</span>
    <span class="contact__line">Glen Harbor, CA 94900</span>
    <span class="contact__line contact__line--strong">www.noravale.com</span>
    <span class="contact__line">nora@noravale.com</span>
    <span class="contact__line contact__line--strong">415.555.0142</span>
    <span class="contact__license">License# MFC48210</span>
  </address>

  <section class="services">
    <h2 class="services__heading">Psychotherapy for<br>Individuals<br>Couples<br>and Families</h2>
    <svg class="services__rule" viewBox="0 0 406 4" aria-hidden="true">
      <line x1="1" y1="2" x2="405" y2="2" stroke="#ffffff" stroke-opacity="0.7" stroke-width="1.2" stroke-dasharray="1.5 4"/>
    </svg>
    <ul class="services__list">
      <li class="services__item">Parenting</li>
      <li class="services__item">Depression</li>
      <li class="services__item">Anxiety</li>
      <li class="services__item">Life Transitions</li>
      <li class="services__item">Divorce</li>
      <li class="services__item">Couples Issues</li>
      <li class="services__item">Women's Issues</li>
      <li class="services__item">Attachment<br>and Neuroscience</li>
    </ul>
  </section>
</main>
</body>
</html>
```